Business card for Luxury Portable Restroom Trailer company

We are a Luxury Portable Restroom Trailer Company Called PELIKAR HIRES. Based in Orange County California. We provide portable restroom trailers for events, such as, Weddings, Concerts, Charity events, Sporting events, Tournaments, Corporate events, ect. We rent and Sell the Luxury restrooms. Our colors are white, grey, and Orange. As you will see in the logo we uploaded.
There are 2 people in the company so the names and titles will change for the 3 people but card will remain the same. Here is the information for each Person: Dennis Moyle CFO 555 018-3647
next Person: Wesley Tanford VP 555 018-3647
Next Person: Miles Tanford CEO 555 018-3647
Information to include on the card: Luxury Restroom Trailers Rental and Sales. Weddings, Concerts, Charity, Sporting and Corp. Events.

```html
<!DOCTYPE html>
<html lang="en">
<head>
<meta charset="utf-8">
<title>PELIKAR HIRES – Business Card</title>
<link href="https://fonts.googleapis.com/css2?family=Montserrat:wght@400;500;700;800&display=swap" rel="stylesheet">
<style>
  :root {
    --orange: #f26d21;
    --grey: #5c5d60;
    --ink: #2b2b2d;
    --paper: #f2f1f0;
    --backdrop: #d9d9db;
  }
  * { box-sizing: border-box; margin: 0; padding: 0; }
  html, body {
    width: 1200px; height: 900px; overflow: hidden;
    background: var(--backdrop);
    font-family: 'Montserrat', Arial, sans-serif;
    color: var(--ink);
  }
  .sheet {
    width: 1200px; height: 900px;
    display: flex; align-items: center; justify-content: center; gap: 30px;
  }
  .card {
    position: relative;
    width: 560px; height: 320px;
    background: var(--paper);
    border-radius: 14px;
    overflow: hidden;
    box-shadow: 0 8px 24px rgba(0,0,0,.18);
  }
  .card-edge {
    position: absolute; left: 0; bottom: 0; width: 100%; height: 14px;
  }

  /* brand name */
  .brand {
    display: flex; align-items: center; gap: 12px;
  }
  .brand-mark {
    width: 16px; height: 16px; background: var(--grey);
  }
  .brand-name {
    font-weight: 800; color: var(--orange); letter-spacing: .04em; white-space: nowrap;
  }

  /* front */
  .card--front .brand {
    position: absolute; left: 70px; top: 98px;
  }
  .card--front .brand-name { font-size: 40px; }
  .tagline {
    position: absolute; right: 40px; top: 198px;
    text-align: right; font-size: 12.5px; line-height: 1.55; font-weight: 400;
  }

  /* back */
  .card--back .brand {
    position: absolute; left: 36px; top: 222px;
  }
  .card--back .brand-mark { width: 10px; height: 10px; }
  .card--back .brand-name { font-size: 20px; }
  .divider {
    position: absolute; left: 300px; top: 44px; width: 1px; height: 150px;
    background: var(--orange);
  }
  .contact {
    position: absolute; left: 322px; top: 42px;
  }
  .contact-name {
    font-size: 21px; font-weight: 700; color: var(--orange); line-height: 1.1;
  }
  .contact-title { font-size: 12px; margin-top: 3px; }
  .contact-address { font-size: 11.5px; line-height: 1.45; margin-top: 10px; }
  .contact-list { list-style: none; margin-top: 10px; font-size: 11.5px; line-height: 1.75; }
  .contact-list li { display: flex; align-items: center; gap: 8px; }
  .contact-list svg { width: 11px; height: 11px; flex: none; }
</style>
</head>
<body>
<main class="sheet">

  <section class="card card--front">
    <div class="brand">
      <span class="brand-mark"></span>
      <span class="brand-name">PELIKAR HIRES</span>
    </div>
    <p class="tagline">
      Luxury Restroom Trailers Rental and Sales.<br>
      Weddings, Concerts, Charity, Sporting, Paeties and Corp Events.
    </p>
    <svg class="card-edge" viewBox="0 0 560 14" preserveAspectRatio="none">
      <polygon points="0,6 370,6 370,14 0,14" fill="var(--orange)"/>
      <polygon points="370,0 560,0 560,14 370,14" fill="var(--grey)"/>
    </svg>
  </section>

  <section class="card card--back">
    <div class="brand">
      <span class="brand-mark"></span>
      <span class="brand-name">PELIKAR HIRES</span>
    </div>
    <div class="divider"></div>
    <div class="contact">
      <p class="contact-name">Miles Tanford</p>
      <p class="contact-title">CEO</p>
      <p class="contact-address">418 Harbor View Rd, #112<br>Lakemont, CA 92704</p>
      <ul class="contact-list">
        <li>
          <svg viewBox="0 0 12 12"><path d="M1 4c0-2 2-3 5-3s5 1 5 3v1H8V4H4v1H1z M2 6h8l1 5H1z" fill="var(--orange)"/></svg>
          555 018-3647
        </li>
        <li>
          <svg viewBox="0 0 12 12"><rect x="3" y="0.5" width="6" height="11" rx="1" fill="none" stroke="var(--orange)" stroke-width="1.2"/><circle cx="6" cy="9.5" r=".8" fill="var(--orange)"/></svg>
          555 018-3647
        </li>
        <li>
          <svg viewBox="0 0 12 12"><rect x="0.5" y="2" width="11" height="8" fill="var(--orange)"/><path d="M0.5 2 6 6.5 11.5 2" fill="none" stroke="var(--paper)" stroke-width="1"/></svg>
          info@pelikarhires.com
        </li>
        <li>
          <svg viewBox="0 0 12 12"><circle cx="6" cy="6" r="5.3" fill="none" stroke="var(--orange)" stroke-width="1.2"/><path d="M0.7 6h10.6M6 0.7c-2.5 3-2.5 7.6 0 10.6M6 0.7c2.5 3 2.5 7.6 0 10.6" fill="none" stroke="var(--orange)" stroke-width="1"/></svg>
          www.pelikarhires.com
        </li>
      </ul>
    </div>
    <svg class="card-edge" viewBox="0 0 560 14" preserveAspectRatio="none">
      <polygon points="0,6 400,6 400,14 0,14" fill="var(--orange)"/>
      <polygon points="400,0 560,0 560,14 400,14" fill="var(--grey)"/>
    </svg>
  </section>

</main>
</body>
</html>
```